Security Officer Training Certifications POSTCARD

We need Post Card Design
-Front and Back
-In Compliance with KOLBEX MAIL for upload!
-For Oversized and Jumbo Size Cards (kolbex mails)

Our Company:
www.northbeamlearningworks.org (FOR IDEAS)

We provide Corporate Security Officer/Criminal Justice/Police Tactics Training for Private Companies that have a security department and officers.

We provide:
Handcuffing certifications
Pepper Spray
Compliance Training
Instructor Training
California Guard Card

FRONT DESIGN TO BE VERY CATCH!
Back of Card List of Services/Menu

Our Card to display powerful image for a Security Officer Department
Traits in Pic and Deigns
VALUE
COMPETITIVE EDGE
PROFESSIONAL GROWTH
QUALITY
PROFICIENT/EFFECTIVE SECURITY OFFICERS
TACTICAL OFFICERS
PROFESSIONALISM
EXPERTS
INDUSTRY LEADERS
READINESS

Target Market(s)

Proprietary Security Officer Department. Agencies that hire their own guard force.
It will be owners of security guard companies, Security Directors, manager

Industry/Entity Type

Security

Requirements
Must have
• GREAT FROM OF CARD PICTURE that encompasses
• Corporate Security Officers
• MUST HAVE A COOL LOOK!
• Professionalism
• Tactical
• The best
• Upgrade skills
• BACK of Card:
• Like list of services with pics and cool stuff
• PICS of Security Officer /Police Professionals
• with great backgrounds!
• COOL
• BACK OF CARD
• Space to have address of receipient
• space for post age
• in ACCORDANCE with KOLBEX MAILS to upload...

```html
<!DOCTYPE html>
<html lang="en">
<head>
<meta charset="utf-8">
<title>Northbeam Learning Works – Security Training Postcard</title>
<link rel="stylesheet" href="https://fonts.googleapis.com/css2?family=Roboto+Condensed:wght@400;700&family=Montserrat:wght@400;600&display=swap">
<style>
  :root {
    --backdrop: #2a2a2c;
    --navy: #2b3a8c;
    --navy-deep: #1f2b6e;
    --royal: #2a62c4;
    --orange: #f08a24;
    --white: #ffffff;
    --photo-light: #c9ccd3;
    --photo-dark: #4a4e58;
    --strip: #dcdde6;
    --ink: #222;
  }
  * { box-sizing: border-box; margin: 0; padding: 0; }
  html, body { width: 900px; height: 1200px; overflow: hidden; }
  body { background: var(--backdrop); position: relative; font-family: "Roboto Condensed", sans-serif; }

  .card { position: absolute; left: 37px; width: 826px; overflow: hidden; }
  .card--front { top: 42px; height: 536px; }
  .card--back { top: 620px; height: 537px; background: var(--white); }

  /* FRONT */
  .front-photo { position: absolute; inset: 0;
    background: linear-gradient(100deg, var(--photo-light) 0%, #9a9ea8 35%, var(--photo-dark) 70%); }
  .front-panel { position: absolute; inset: 0; }
  .top-band { position: absolute; left: 0; top: 43px; width: 826px; height: 76px;
    background: var(--royal); display: flex; align-items: center; justify-content: flex-end; padding-right: 24px; }
  .top-band p { color: var(--white); font-size: 21.5px; line-height: 1.25; text-transform: uppercase; text-align: left; width: 620px; }
  .brand { position: absolute; left: 22px; top: 18px; width: 124px; height: 124px; border-radius: 50%;
    background: var(--white); border: 4px solid var(--navy); display: flex; align-items: center; justify-content: center; text-align: center; }
  .brand span { color: var(--navy); font-weight: 700; font-size: 15px; line-height: 1.1; text-transform: uppercase; }
  .provide-tag { position: absolute; right: 0; top: 156px; width: 245px; height: 36px; background: var(--orange);
    clip-path: polygon(18px 0, 100% 0, 100% 100%, 18px 100%, 0 50%);
    color: var(--white); font-size: 25px; line-height: 36px; padding-left: 40px; letter-spacing: .5px; }
  .services { position: absolute; right: 25px; top: 206px; list-style: none; text-align: right; }
  .services li { color: var(--white); font-size: 27px; line-height: 37.5px; }
  .services li::before { content: "✓"; color: var(--orange); margin-right: 4px; }
  .call-front { position: absolute; right: 25px; top: 410px; color: var(--white); font-weight: 700; font-size: 40px; }
  .cert-strip { position: absolute; left: 378px; top: 470px; width: 448px; height: 56px; background: var(--strip);
    display: flex; align-items: center; justify-content: space-around; }
  .cert-shape { width: 44px; height: 40px; background: #8c6b3f; border-radius: 8px; }
  .cert-shape--red { background: #b32a2a; border-radius: 50%; }
  .cert-shape--grey { background: #7a7a80; width: 30px; }

  /* BACK */
  .back-panel { position: absolute; inset: 0; }
  .back-text { position: absolute; left: 24px; top: 20px; color: var(--white); font-family: "Montserrat", sans-serif; }
  .back-head { font-size: 16.5px; line-height: 22px; text-transform: uppercase; }
  .prices { list-style: none; margin-top: 8px; padding-left: 2px; font-size: 14px; line-height: 18px; }
  .prices li { margin-bottom: 7px; }
  .pitch { font-size: 18.5px; font-weight: 600; line-height: 24px; margin-top: 8px; }
  .contact { font-size: 17px; line-height: 23px; margin-top: 16px; }
  .badge { position: absolute; border-radius: 50%; background: var(--white); border: 6px solid var(--navy);
    display: flex; align-items: center; justify-content: center; }
  .badge i { display: block; width: 55%; height: 55%; border-radius: 50%; }
  .badge--gold { left: 402px; top: 110px; width: 100px; height: 100px; }
  .badge--gold i { background: #d4a93a; }
  .badge--silver { left: 366px; top: 232px; width: 108px; height: 108px; }
  .badge--silver i { background: #b8bcc4; }
  .stamp-box { position: absolute; left: 730px; top: 25px; width: 71px; height: 76px; border: 1px solid var(--ink); }
</style>
</head>
<body>

<section class="card card--front">
  <div class="front-photo" role="img" aria-label="Photo of a uniformed security officer in a cap talking on a radio and pointing across a city street"></div>
  <svg class="front-panel" width="826" height="536" viewBox="0 0 826 536" aria-hidden="true">
    <polygon points="555,0 826,0 826,536 340,536" fill="#2b3a8c" opacity=".92"/>
  </svg>
  <div class="top-band">
    <p>We provide corporate security officer/criminal justice/police tactics training for private companies that have a security department and officers.</p>
  </div>
  <div class="brand"><span>Northbeam<br>Learning<br>Works</span></div>
  <div class="provide-tag">WE PROVIDE:</div>
  <ul class="services">
    <li>Handcuffing certifications</li>
    <li>Pepper Spray</li>
    <li>Compliance Training</li>
    <li>Instructor Training</li>
    <li>California Guard Card</li>
  </ul>
  <div class="call-front">CALL NOW (555) 014-2290</div>
  <div class="cert-strip">
    <span class="cert-shape"></span>
    <span class="cert-shape cert-shape--red"></span>
    <span class="cert-shape cert-shape--grey"></span>
  </div>
</section>

<section class="card card--back">
  <svg class="back-panel" width="826" height="537" viewBox="0 0 826 537" aria-hidden="true">
    <defs>
      <linearGradient id="backBlue" x1="0" y1="0" x2="0" y2="1">
        <stop offset="0" stop-color="#2f3f95"/>
        <stop offset="1" stop-color="#1f2b6e"/>
      </linearGradient>
    </defs>
    <polygon points="0,0 528,0 348,537 0,537" fill="url(#backBlue)"/>
    <rect x="0" y="0" width="520" height="88" fill="#2a62c4" opacity=".55"/>
    <polygon points="400,380 350,537 440,537" fill="#2a62c4"/>
  </svg>
  <div class="back-text">
    <div class="back-head">Security Corporate Training<br>On-Site – Seminars – Group Settings<br>Regulatory &amp; Compliance</div>
    <ul class="prices">
      <li>Tactical Handcuffing:<br>$1000 for up to 20 personnel</li>
      <li>Chemical Agents (Pepper Spray)<br>$1000 for up to 20 personnel</li>
      <li>Baton Training (Expandable) Refresher Training<br>$1650 for up to 20 personnel<br>(NOT INCLUDING $50 BATON<br>PERMIT FEE per Student!)</li>
      <li>Active Shooter Training<br>$1650 for up to 20 personnel</li>
    </ul>
    <p class="pitch">On-Site – We come to you –<br>SAVE on Staff Training with our<br>compliance &amp; training Seminars</p>
    <p class="contact">Call now 555-014-2290<br>www.northbeamlearningworks.org<br>State Security Training Lic #NBL 4107</p>
  </div>
  <div class="badge badge--gold" role="img" aria-label="Gold security officer badge"><i></i></div>
  <div class="badge badge--silver" role="img" aria-label="Silver security officer badge"><i></i></div>
  <div class="stamp-box" aria-label="Postage area"></div>
</section>

</body>
</html>
```